Mara Fenwick Music EP Design Artwork

EP musical recording cover art work. Mara Fenwick is a new artist in the Pop, Country Pop, Pop Rock, Americana and Singer-songwriter genres. The name of the EP is "Quiet Harbor Lights", and her first single is being released on all streaming platforms globally June 1st. We are looking for a graphic design that has that Pop/rock female artist appeal. marafenwick.com and all social media outlets are marafenwickmusic (reference). Your art work will be seen globally and we will give a personal shout out on all her socials to the design we select as a single post. Her signature logo is attached for a color and style example. Please try to use the signature within the EP cover design, but feel free to change the purple backing accordingly if another color is needed to fit better with the color scheme of your design.

Requirements
Must have
• Mara Fenwick signature logo and EP name

Some of you asked for hi res pics, use this link:

https://files.sharevault-example.net/folders/8kTr2WqLp4ZxNc7VbHd3MfYs1JaGe9Ro
Should not have
• June 1 on the EP art work. June 1 is the release of the first single on the EP. This is an album cover, we want it to look like a really cool pop female artist album cover, thanks.

```html
<!DOCTYPE html>
<html lang="en">
<head>
<meta charset="utf-8">
<title>Quiet Harbor Lights – Mara Fenwick</title>
<link rel="stylesheet" href="https://fonts.googleapis.com/css2?family=Oswald:wght@400;700&display=swap">
<style>
  :root {
    --stage: #a3a3a3;
    --sun-deep: #e9d877;
    --sun-light: #f5eeb0;
    --title-white: #ffffff;
    --title-shadow: rgba(196, 184, 104, 0.75);
    --hair: #b5894f;
    --jacket: #1b1a1a;
    --skin: #e7b9a0;
  }
  * { margin: 0; padding: 0; box-sizing: border-box; }
  html, body {
    width: 1200px;
    height: 900px;
    overflow: hidden;
    background: var(--stage);
  }
  .ep-cover {
    position: absolute;
    left: 190px;
    top: 40px;
    width: 820px;
    height: 820px;
    overflow: hidden;
    background: linear-gradient(160deg, var(--sun-deep) 0%, var(--sun-light) 100%);
    box-shadow: 0 14px 30px rgba(0, 0, 0, 0.25);
  }
  .artist-portrait {
    position: absolute;
    left: 0;
    top: 30px;
    width: 400px;
    height: 790px;
    display: block;
  }
  .ep-title {
    position: absolute;
    right: 4px;
    bottom: -22px;
    text-align: right;
    font-family: "Oswald", "Arial Narrow", sans-serif;
    font-weight: 700;
    font-size: 205px;
    line-height: 0.98;
    letter-spacing: -4px;
    text-transform: uppercase;
    color: var(--title-white);
    text-shadow: 10px 12px 0 var(--title-shadow);
  }
  .ep-title span { display: block; }
  .artist-signature {
    position: absolute;
    left: 44px;
    bottom: 42px;
    font-family: "Oswald", "Arial Narrow", sans-serif;
    font-weight: 400;
    font-size: 32px;
    letter-spacing: 1px;
    color: var(--title-white);
  }
</style>
</head>
<body>
  <main class="ep-cover">
    <svg class="artist-portrait" viewBox="0 0 400 790" role="img" aria-label="Portrait photo of Mara Fenwick smiling, in a black jacket and patterned turtleneck">
      <defs>
        <linearGradient id="portrait-tones" x1="0" y1="0" x2="0" y2="1">
          <stop offset="0" stop-color="var(--hair)" stop-opacity="0.85"/>
          <stop offset="0.35" stop-color="var(--skin)" stop-opacity="0.8"/>
          <stop offset="0.62" stop-color="var(--jacket)"/>
          <stop offset="1" stop-color="var(--jacket)"/>
        </linearGradient>
      </defs>
      <rect width="400" height="790" fill="url(#portrait-tones)"/>
    </svg>

    <h1 class="ep-title">
      <span>Quiet</span>
      <span>Harbor</span>
      <span>Lights</span>
    </h1>

    <p class="artist-signature">Mara Fenwick</p>
  </main>
</body>
</html>
```